Quiet Myrrhwood product line - spa line

This is the first few new layouts I need. If I like what I get I have multiple other collections that I am rebranding. Label & boxes for 2 Quiet Myrrhwood products
https://velvetgroveapothecary.ca/collections/quiet-myrrhwood-skin-care-collection
the first 2 products in this line need a new box and the Hydrosol needs a new label. I am looking for a minimal illustration that speaks to both men and women. The info on the box is the same except the word Organic is to be replaced with Botanical.

Target Market(s)

30yr-60yr men and women...but mostly women

Industry/Entity Type

natural skincare / wholefoods / spas

Font styles to use
Sans Serif
Decorative
Script

Colors
0054AA
0677BA
7BADD7
CADEEF
E8F1F8
FFC000
F8CF3A
FAE287
FDF2CF
FEFAEE

Requirements
Must have
• muted soft background color. logo and all text that is presently on the label. go here: https://velvetgroveapothecary.ca/collections/quiet-myrrhwood-skin-care-collection
Nice to have
• botanical illustration but also with a clean minimal spa look...design continueing on inside of box. Royal Cobalt Blue foil or Gold foil for logo
Should not have
• hot bright florescent color

```html
<!DOCTYPE html>
<html lang="en">
<head>
<meta charset="UTF-8">
<title>Quiet Myrrhwood – Hydrosol Mist Box Front</title>
<link href="https://fonts.googleapis.com/css2?family=Tenor+Sans&display=swap" rel="stylesheet">
<style>
  :root {
    --page: #ffffff;
    --ink: #1d1d1d;
    --gold: #f5c21b;
    --gold-line: #a88a3e;
    --gold-soft: #d9c79a;
    --dieline: #e5393b;
  }
  * { margin: 0; padding: 0; box-sizing: border-box; }
  html, body {
    width: 1200px;
    height: 1200px;
    overflow: hidden;
    background: var(--page);
  }
  .canvas {
    position: relative;
    width: 1200px;
    height: 1200px;
    font-family: "Tenor Sans", sans-serif;
    color: var(--ink);
  }
  .box-front {
    position: absolute;
    left: 397px;
    top: 50px;
    width: 406px;
    height: 1100px;
    border: 1.5px solid var(--dieline);
    background: var(--page);
    overflow: hidden;
  }
  .brand-name {
    position: absolute;
    top: 78px;
    left: 0;
    width: 100%;
    text-align: center;
    font-size: 21px;
    letter-spacing: 0.12em;
    text-transform: uppercase;
    color: var(--ink);
  }
  .brand-dot {
    position: absolute;
    top: 272px;
    left: 122px;
    width: 116px;
    height: 116px;
    border: 3px solid var(--gold);
    border-radius: 50%;
  }
  .botanical-art {
    position: absolute;
    top: 205px;
    right: 0;
    width: 128px;
    height: 875px;
    background: linear-gradient(to left, rgba(168,138,62,0.55), rgba(217,199,154,0.25) 70%, rgba(255,255,255,0));
  }
  .product-title {
    position: absolute;
    top: 498px;
    left: 0;
    width: 100%;
    text-align: center;
    text-transform: uppercase;
  }
  .title-line { display: block; line-height: 1; }
  .title-range {
    font-size: 35px;
    letter-spacing: 0.18em;
    padding-left: 40px;
  }
  .title-accent {
    margin-top: 22px;
    font-size: 56px;
    letter-spacing: 0.12em;
    color: var(--gold);
  }
  .title-name {
    margin-top: 22px;
    font-size: 30px;
    letter-spacing: 0.2em;
  }
  .product-details {
    position: absolute;
    top: 862px;
    left: 0;
    width: 100%;
    text-align: center;
    text-transform: uppercase;
  }
  .detail-type { font-size: 22px; letter-spacing: 0.02em; }
  .detail-claims { margin-top: 6px; font-size: 15px; letter-spacing: 0.06em; word-spacing: 0.3em; }
  .detail-french { margin-top: 22px; font-size: 32px; letter-spacing: 0.01em; }
</style>
</head>
<body>
  <main class="canvas">
    <section class="box-front">
      <div class="botanical-art" role="img" aria-label="Gold line engraving of daisy flowers, buds and serrated leaves running down the right edge"></div>
      <p class="brand-name">Velvet Grove Apothecary</p>
      <div class="brand-dot" aria-hidden="true"></div>
      <h1 class="product-title">
        <span class="title-line title-range">Botanical</span>
        <span class="title-line title-accent">Quiet</span>
        <span class="title-line title-name">Myrrhwood</span>
      </h1>
      <div class="product-details">
        <p class="detail-type">Hydrosol Mist</p>
        <p class="detail-claims">Correct Protect Replenish</p>
        <p class="detail-french">L’Eau Pour Visage</p>
      </div>
    </section>
  </main>
</body>
</html>
```